Candle company needs a label for candle

Looking for a designer to create my candle label. I am going to attach a few pictures of my vision for the label as well as my Company Logo and jar I have puchased. I'm going for the modern rustic feel but you are the designer and have full trust in your abilities. The label is going to be printed on Kraft paper (2x3) so looking for the font to be black. The candle label MUST include the following information:
Wick Harbor Co.
NO. 01: Eucalyptus + Spearmint
Handmade In NJ
Soy Wax
9oz

Industry/Entity Type

Candle Industry

Colors

Designer to choose colors to be used in the design.

Requirements
Should not have
• Any images

```html
<!DOCTYPE html>
<html lang="en">
<head>
<meta charset="utf-8">
<title>Wick Harbor Co. — Candle Label</title>
<link href="https://fonts.googleapis.com/css2?family=Questrial&family=Dancing+Script:wght@500&display=swap" rel="stylesheet">
<style>
  :root {
    --page-bg: #ffffff;
    --kraft: #cbb690;
    --kraft-edge: #bda77f;
    --ink: #333231;
  }
  html, body {
    margin: 0;
    padding: 0;
    width: 1200px;
    height: 1026px;
    overflow: hidden;
    background: var(--page-bg);
  }
  .canvas {
    position: relative;
    width: 1200px;
    height: 1026px;
  }
  .label {
    position: absolute;
    left: 150px;
    top: 223px;
    width: 900px;
    height: 580px;
    background: var(--kraft);
    box-shadow: inset 0 0 0 1px var(--kraft-edge);
    color: var(--ink);
    font-family: "Questrial", sans-serif;
  }
  .label > * {
    position: absolute;
    left: 0;
    width: 100%;
    text-align: center;
    margin: 0;
  }
  .brand-name {
    top: 150px;
    font-size: 44px;
    line-height: 1;
  }
  .scent-number {
    top: 262px;
    font-size: 38px;
    line-height: 1;
  }
  .scent-name {
    top: 312px;
    font-size: 40px;
    line-height: 1;
  }
  .origin {
    top: 380px;
    left: 225px;
    width: 470px;
    height: 58px;
    border-top: 1.5px solid var(--ink);
    border-bottom: 1.5px solid var(--ink);
    box-sizing: border-box;
    font-size: 46px;
    line-height: 54px;
    letter-spacing: 1px;
  }
  .wax {
    top: 462px;
    font-family: "Dancing Script", cursive;
    font-size: 40px;
    line-height: 1;
  }
  .weight {
    top: 524px;
    font-size: 27px;
    line-height: 1;
  }
</style>
</head>
<body>
  <main class="canvas">
    <section class="label">
      <p class="brand-name">Wick Harbor Co.</p>
      <p class="scent-number">NO. 01:</p>
      <p class="scent-name">Eucalyptus + Spearmint</p>
      <p class="origin">Handmade In NJ</p>
      <p class="wax">Soy Wax</p>
      <p class="weight">9oz</p>
    </section>
  </main>
</body>
</html>
```